Box for baby swaddle blankets.

Hi there!

I'd like you to make a packaging design for the box of my muslin swaddle blankets which I'll be selling on Pindlewick.com. I want the product to be the perfect baby shower gift! Most of the packages of my competitors are made by the manufacturing company, so they're pretty simple and similar to each other, I'd like you to make a unique design for me. I included a detailed description about the parameters in the "must haves" section. If you have any questions or suggestions, please message me.

Target Market(s)

Pindlewick.com

Industry/Entity Type

Baby Care

Colors

Designer to choose colors to be used in the design.

Requirements
Must have
• 1. Most of my competitors use pretty basic packaging, so I'd like stand out with my box. I was thinking about putting my logo at the bottom of the front side, and make heart-shaped cuts above the elephant's trunk, which would allow buyers to see the fabric and the pattern of the blankets. You can remove the heart from my logo since I think it wouldn't look good with the cuts above it. Tell me what you think about this, I'm also open for other ideas for the front as well as long as it makes the packaging unique and gives the buyers a peek of the blankets.
• I attached some examples of cuts I've seen on packages.
• 2. I'd like you to use the title BABY SWADDLE BLANKETS and my logo on the front. The package contains 3 blankets are made from organic muslin cotton with 47x47 inch size, you could include this also in the front if you can find a good way for it .
• Also, I'd like to have a stamp of 100% ORGANIC COTTON in one corner.
• The package will contain a bonus baby bandana bib, so please put a BANDANA BIB GIFT INSIDE! object with an arrow pointing in the box in the front.
• 3. For the sides, one of them should show the different ways you can use these blankets, with illustrations. I'll attach some examples for this (I like the pictogram-type illustration on img1 better) . You can add my logo for the top side. You can try to add the words "BREATHABLE" "EXTRA SOFT" "LARGE SIZE" "100% ORGANIC COTTON" on the remaining side(s) if it would look good in your opinion.
• 4. For the back, I'd like you to add a 4-step instruction about how to swaddle the baby with the blankets. Since almost all of competitors use the same images, I'd like you to design new ones, make it playful and baby-friendly :) I'll attach some examples for these instructions as well.. The bottom of the back should contain the text "Made with care in China, designed with love in the United States" and a place for the barcode.
• 4. The box should be the size of 21*22*8 in centimeters.
• If you have any questions or suggestions for the design, please message me.
Nice to have
• If you have any other ideas or suggestions about the design, feel free to contact me.

```html
<!DOCTYPE html>
<html lang="en">
<head>
<meta charset="utf-8">
<title>Baby Swaddle Blankets – Box Front</title>
<link href="https://fonts.googleapis.com/css2?family=Shadows+Into+Light+Two&family=Gochi+Hand&family=Courier+Prime:wght@700&display=swap" rel="stylesheet">
<style>
  :root {
    --canvas: #f3f5f5;
    --box-teal: #98d5d2;
    --window-blue: #e1f3fb;
    --band-blue: #a9def8;
    --heart-light: #f4fafb;
    --heart-teal: #bfe3e0;
    --heart-sky: #cfe8f3;
    --ink-white: #ffffff;
    --ink-blue: #1f78b8;
    --stamp-green: #3f8f32;
    --brand-blue: #7fb4e2;
  }
  html, body {
    margin: 0;
    width: 1200px;
    height: 1000px;
    overflow: hidden;
    background: var(--canvas);
  }
  .box-front {
    position: absolute;
    left: 262px;
    top: 134px;
    width: 680px;
    height: 732px;
  }
  .box-front svg { display: block; width: 100%; height: 100%; }
  .face { fill: var(--box-teal); }
  .peek-window { fill: var(--window-blue); }
  .gift-band { fill: var(--band-blue); }
  .gift-note {
    font-family: "Gochi Hand", cursive;
    font-size: 21px;
    fill: var(--ink-blue);
    letter-spacing: 1px;
  }
  .gift-arrow { fill: none; stroke: var(--ink-blue); stroke-width: 2.4; stroke-linecap: round; stroke-linejoin: round; }
  .organic-stamp rect { fill: none; stroke: var(--stamp-green); stroke-width: 4; }
  .organic-stamp text {
    font-family: "Courier Prime", monospace;
    font-weight: 700;
    font-size: 21px;
    fill: var(--stamp-green);
  }
  .brand-name {
    font-family: "Shadows Into Light Two", cursive;
    font-size: 44px;
    fill: var(--brand-blue);
  }
  .brand-dot { fill: var(--brand-blue); }
  .product-title {
    font-family: "Shadows Into Light Two", cursive;
    font-size: 31px;
    fill: var(--ink-white);
  }
  .product-sub {
    font-family: "Shadows Into Light Two", cursive;
    font-size: 24px;
    fill: var(--ink-white);
  }
  .pack-heart { fill: var(--band-blue); }
  .pack-count {
    font-family: "Shadows Into Light Two", cursive;
    font-size: 26px;
    fill: var(--ink-white);
  }
</style>
</head>
<body>
<div class="box-front">
  <svg viewBox="0 0 595 640" xmlns="http://www.w3.org/2000/svg">
    <defs>
      <symbol id="heart-cut" viewBox="0 0 100 92">
        <path d="M50,90 C20,70 0,52 0,28 C0,12 12,0 27,0 C38,0 46,7 50,15 C54,7 62,0 73,0 C88,0 100,12 100,28 C100,52 80,70 50,90Z"/>
      </symbol>
      <linearGradient id="fabric-teal" x1="0" y1="0" x2="1" y2="1">
        <stop offset="0" stop-color="var(--heart-light)"/>
        <stop offset="1" stop-color="var(--heart-teal)"/>
      </linearGradient>
      <linearGradient id="fabric-sky" x1="0" y1="0" x2="0" y2="1">
        <stop offset="0" stop-color="var(--heart-sky)"/>
        <stop offset="1" stop-color="var(--heart-light)"/>
      </linearGradient>
    </defs>

    <rect class="face" x="0" y="0" width="595" height="640"/>
    <rect class="peek-window" x="87" y="45" width="425" height="420"/>
    <path class="gift-band" d="M0,222 C90,380 210,462 320,462 C430,462 520,400 595,312 L595,362 C470,480 290,560 0,575 Z"/>
    <path class="face" d="M595,362 C470,480 290,560 0,575 L0,640 L595,640 Z"/>

    <g role="img" aria-label="Blanket fabric with tree pattern seen through heart cut-out">
      <use href="#heart-cut" x="92" y="62" width="125" height="175" fill="url(#fabric-teal)"/>
    </g>
    <g role="img" aria-label="Blanket fabric with whale pattern seen through heart cut-out">
      <use href="#heart-cut" x="302" y="62" width="155" height="175" fill="url(#fabric-teal)"/>
    </g>
    <g role="img" aria-label="Blanket fabric with sun and wave pattern seen through heart cut-out">
      <use href="#heart-cut" x="236" y="308" width="170" height="150" fill="url(#fabric-sky)"/>
    </g>

    <text class="gift-note" x="14" y="400">BANDANA BIB</text>
    <text class="gift-note" x="34" y="426">GIFT INSIDE!</text>
    <path class="gift-arrow" d="M96,468 C140,486 180,478 208,446"/>
    <path class="gift-arrow" d="M194,448 L209,444 L210,460"/>

    <g class="organic-stamp" transform="rotate(-8 480 402)">
      <rect x="390" y="382" width="182" height="40" rx="3"/>
      <text x="481" y="409" text-anchor="middle">100% ORGANIC</text>
    </g>

    <circle class="brand-dot" cx="392" cy="543" r="7"/>
    <text class="brand-name" x="410" y="558">Snugglory</text>

    <text class="product-title" x="14" y="585">Baby Swaddle Blankets</text>
    <path class="pack-heart" d="M40,636 C20,624 10,614 10,602 C10,594 16,588 24,588 C30,588 36,592 40,598 C44,592 50,588 56,588 C64,588 70,594 70,602 C70,614 60,624 40,636Z"/>
    <text class="pack-count" x="33" y="623">3</text>
    <text class="product-sub" x="72" y="622">Pack Muslin Blanket</text>
  </svg>
</div>
</body>
</html>
```